Cleaning Company needs a new business card design

Hi, We are looking for new business card designs to update with our latest logo and company information.
We would like to see designs using the colours:
Royal Blue #4169E1 - this is our company colour so this has to be in there. Please feel free to experiment with other colours.
Must include:
Front of business card:
Logo
Back of the business card:
0800 529 6081
07438 915 702
Email: info@pkrtidyhomes.co.uk
Web: www.pkrtidyhomes.co.uk
Services:
End of Tenancy
Carpet & Upholstery
Regular & One Off
all work fully insured.
The front of the business card with the logo can be made to look raised print. The blue man to be a shiny finish.
The business card needs to be presented in a matt finish
The business must be in the following styles:
Standard Square with rounded corners.
Thank you to all that take part in this.
Target Market(s)
Men and Women of different ages in the UK.
Industry/Entity Type
House Cleaning
Contact Information for Business Card
Front of business card:
Logo
0800 529 6081
07438 915 702
Email: pkrtidy@mailbox-demo.co.uk
Services:
End of Tenancy
Carpet & Upholstery
Regular & One Off
all work fully insured.

```html
<!DOCTYPE html>
<html lang="en">
<head>
<meta charset="utf-8">
<title>pkr Tidy Homes Limited – Business Card</title>
<link href="https://fonts.googleapis.com/css2?family=Questrial&family=Arimo:wght@400&display=swap" rel="stylesheet">
<style>
  :root {
    --backdrop: #ececec;
    --brand-navy: #3b418e;
    --brand-sky: #2aa3dc;
    --card-cream: #f3f3ec;
    --card-cream-shade: #e4e4dc;
    --ink: #2a2a2a;
    --white: #ffffff;
    --band-text: #d9dbef;
  }
  * { box-sizing: border-box; margin: 0; padding: 0; }
  html, body {
    width: 1200px; height: 1200px; overflow: hidden;
    background: var(--backdrop);
  }
  .canvas { position: relative; width: 1200px; height: 1200px; }

  .card {
    position: absolute;
    border-radius: 10px;
    overflow: hidden;
    box-shadow: 0 6px 18px rgba(0,0,0,0.12);
  }

  /* Back of card – portrait */
  .card-back {
    left: 120px; top: 320px;
    width: 330px; height: 560px;
    background: linear-gradient(180deg, var(--card-cream) 0%, var(--card-cream) 60%, var(--card-cream-shade) 100%);
  }
  .back-content {
    position: absolute; top: 16px; right: 18px;
    height: 460px;
    writing-mode: vertical-rl;
  }
  .back-brand .brand-name {
    display: block;
    font-family: "Questrial", sans-serif;
    font-size: 88px; line-height: 0.95;
    color: var(--brand-navy);
  }
  .back-brand .brand-sub {
    display: block;
    font-family: "Questrial", sans-serif;
    font-size: 15px; line-height: 1.3;
    color: var(--brand-navy);
  }
  .services {
    margin-right: 34px;
    font-family: "Arimo", sans-serif;
    font-size: 15px; line-height: 1.2; color: var(--ink);
    list-style: none;
  }
  .services li { display: block; }
  .contact-band {
    position: absolute; left: 0; right: 0; bottom: 0;
    height: 68px;
    background: var(--brand-navy);
    padding: 8px 14px;
    font-family: "Arimo", sans-serif;
    font-size: 10.5px; line-height: 1.22;
    color: var(--band-text);
  }

  /* Front of card – landscape */
  .card-front {
    left: 490px; top: 430px;
    width: 590px; height: 340px;
    background: var(--brand-navy);
    display: flex; align-items: center; justify-content: center;
  }
  .front-brand { display: flex; flex-direction: column; align-items: flex-start; }
  .front-brand .brand-row { display: flex; align-items: center; gap: 14px; }
  .front-brand .brand-name {
    font-family: "Questrial", sans-serif;
    font-size: 150px; line-height: 0.85;
    color: var(--white);
  }
  .brand-dot {
    width: 38px; height: 38px; border-radius: 50%;
    background: var(--brand-sky);
    margin-top: 8px;
  }
  .front-brand .brand-sub {
    font-family: "Questrial", sans-serif;
    font-size: 26px; color: var(--white);
    margin-top: 8px; padding-left: 30px;
  }
</style>
</head>
<body>
<main class="canvas">
  <section class="card card-back" aria-label="Back of business card">
    <div class="back-content">
      <div class="back-brand">
        <span class="brand-name">pkr</span>
        <span class="brand-sub">Tidy Homes Limited</span>
      </div>
      <ul class="services">
        <li>Services:</li>
        <li>End of Tenancy</li>
        <li>Carpet &amp; Upholstery</li>
        <li>Regular &amp; One Off</li>
      </ul>
    </div>
    <div class="contact-band">
      <p>0800 529 6081</p>
      <p>07438 915 702</p>
      <p>info@pkrtidyhomes.co.uk</p>
      <p>www.pkrtidyhomes.co.uk</p>
    </div>
  </section>

  <section class="card card-front" aria-label="Front of business card">
    <div class="front-brand">
      <div class="brand-row">
        <span class="brand-name">pkr</span>
        <span class="brand-dot"></span>
      </div>
      <span class="brand-sub">Tidy Homes Limited</span>
    </div>
  </section>
</main>
</body>
</html>
```